Re-design of website

I have an existing website that I would like to improve. The functionality will remain the same but the overall look will need to be changed. I have some ideas of what i would like included and am also in need of someone else to input their own creative ideas. I am on a tight deadline to get these improvements made as I have many people being directed to the site via our advertising campaigns that are in full swing late next week. Thanks
Target Market(s)
The website provides a virtual space for families to learn more about our learning program which we operate out of Dubai and will soon spread to the other Emirates. The families are generally between 25-50 year old parents with children up to the age of 6. They are local Emirati's as well as expats.

```html
<!DOCTYPE html>
<html lang="en">
<head>
<meta charset="utf-8">
<title>Bright Sprouts Accelerated Learning Centre</title>
<link href="https://fonts.googleapis.com/css2?family=Open+Sans:wght@400;600;700&display=swap" rel="stylesheet">
<style>
  :root {
    --orange-top: #f9bb3a;
    --orange-bottom: #ee9418;
    --red-active: #d2300c;
    --heading-red: #c8290b;
    --accent-orange: #ef4a0c;
    --body-text: #555555;
    --nav-divider: #f7c664;
    --sky-blue: #3db8e3;
    --cloud-light: #e4f5fd;
    --cloud-mid: #c6e9fa;
    --box-border: #d6d6d6;
    --footer-bg: #eeeeee;
    --footer-text: #555555;
    --white: #ffffff;
  }
  * { box-sizing: border-box; margin: 0; padding: 0; }
  html, body { width: 1200px; height: 770px; overflow: hidden; background: var(--white); }
  body { position: relative; font-family: "Open Sans", Verdana, sans-serif; color: var(--body-text); }

  .main-nav {
    position: absolute; left: 125px; top: 0; width: 951px; height: 42px;
    display: flex; border-radius: 0 0 8px 8px; overflow: hidden;
    background: linear-gradient(var(--orange-top), var(--orange-bottom));
  }
  .nav-shadow {
    position: absolute; left: 145px; top: 42px; width: 912px; height: 12px;
    background: radial-gradient(ellipse at top, rgba(0,0,0,.45), rgba(0,0,0,0) 70%);
  }
  .nav-item {
    color: var(--white); font-weight: 700; font-size: 13px; text-decoration: none;
    display: flex; align-items: center; justify-content: center; height: 42px;
    border-right: 1px solid var(--nav-divider);
  }
  .nav-item:last-child { border-right: none; }
  .nav-item.is-active { background: linear-gradient(#e0400d, var(--red-active)); }

  .cloud {
    position: absolute; border-radius: 50px;
    background: linear-gradient(var(--cloud-light), var(--cloud-mid));
  }

  .intro { position: absolute; left: 125px; top: 78px; width: 614px; }
  .section-title { font-size: 26px; font-weight: 400; color: var(--heading-red); line-height: 34px; margin-bottom: 6px; }
  .section-title strong { font-weight: 700; }
  .intro p { font-size: 12px; line-height: 18px; text-align: justify; margin-bottom: 18px; }
  .intro .mission-title { margin-top: 0; }

  .side-box {
    position: absolute; left: 861px; width: 214px; border: 1px solid var(--box-border);
    border-radius: 8px; background: linear-gradient(#ffffff, #ececec);
  }
  .register-box { top: 84px; height: 134px; }
  .register-text { position: absolute; left: 11px; top: 45px; color: var(--heading-red); font-size: 15px; line-height: 18px; }
  .register-text strong { display: block; font-size: 14px; font-weight: 700; }
  .register-art {
    position: absolute; right: 8px; top: 8px; width: 80px; height: 116px; border-radius: 8px;
    background: linear-gradient(#f4c9a0, #c97c3b);
  }
  .contact-box { top: 242px; height: 134px; padding: 12px 14px; }
  .contact-title { font-size: 17px; font-weight: 400; color: var(--heading-red); }
  .contact-title strong { font-weight: 700; }
  .contact-address { font-size: 12px; line-height: 16px; margin-top: 4px; padding-left: 2px; }
  .contact-phone { margin-top: 12px; padding-left: 2px; font-size: 15px; color: var(--heading-red); }
  .contact-phone span { color: #777777; font-weight: 700; font-size: 14px; }

  .talents { position: absolute; left: 125px; top: 430px; width: 950px; height: 205px; }
  .talent { position: absolute; top: 0; width: 140px; text-align: center; }
  .talent-label { font-size: 13px; font-weight: 700; color: var(--accent-orange); line-height: 20px; }
  .talent-label.is-center { color: var(--heading-red); }
  .talent-arrow { display: block; margin: 6px auto 0; }
  .talent-figure { width: 86px; height: 110px; margin: 6px auto 0; border-radius: 30px 30px 8px 8px; }
  .talent-stand { display: block; margin: -12px auto 0; }

  .site-footer {
    position: absolute; left: 0; top: 655px; width: 1200px; height: 115px;
    background: var(--footer-bg); text-align: center;
  }
  .copyright { margin-top: 29px; font-size: 12px; color: var(--footer-text); }
  .copyright strong { font-weight: 700; }
  .social-links { display: flex; justify-content: center; gap: 10px; margin-top: 10px; }
  .social-dot { width: 30px; height: 30px; border-radius: 50%; }
</style>
</head>
<body>
  <nav class="main-nav">
    <a class="nav-item is-active" style="width:101px">Home</a>
    <a class="nav-item" style="width:154px">Oue Method</a>
    <a class="nav-item" style="width:156px">The Program</a>
    <a class="nav-item" style="width:102px">Media</a>
    <a class="nav-item" style="width:132px">About Us</a>
    <a class="nav-item" style="width:140px">Contact Us</a>
    <a class="nav-item" style="width:166px">News &amp; Events</a>
  </nav>
  <div class="nav-shadow"></div>

  <div class="cloud" role="img" aria-label="Soft cloud" style="left:518px;top:70px;width:68px;height:32px"></div>
  <div class="cloud" role="img" aria-label="Soft cloud" style="left:735px;top:166px;width:98px;height:46px"></div>
  <div class="cloud" role="img" aria-label="Soft cloud" style="left:25px;top:266px;width:110px;height:64px"></div>
  <div class="cloud" role="img" aria-label="Soft cloud" style="left:1050px;top:344px;width:120px;height:62px"></div>

  <main class="intro">
    <h1 class="section-title"><strong>Welcome</strong> to Our Site</h1>
    <p>Research and leading academics agree that the early years of a child's life (defined as the 6 month old to 6 year old age group) is a critical time period to enhance the emotional and intellectual IQ of a child. 80% of your child's brain is developed by the age of 6 years old, to not offer heightened stimulation and specifically, right brain training during this period means that your child will not use a high proportion of their brain in their life time.</p>
    <p>Bright Sprouts Accelerated Learning Centre is the first a whole brain training program designed to maximise your child's potential during this key period of development.</p>
    <h2 class="section-title mission-title"><strong>Our</strong> Mission</h2>
    <p>At Bright Sprouts, our philosophy and curriculum supports like-minded parents who want happiness for their children and want to see their children become the best they can be in their life. Our children are happy, confident and content with inquisitive minds and life skills that form the foundation of their lifetime of development and learning.</p>
  </main>

  <aside class="side-box register-box">
    <div class="register-text">Register your<strong>Interest Today</strong></div>
    <div class="register-art" role="img" aria-label="Illustration of a boy reading at a school desk"></div>
  </aside>

  <aside class="side-box contact-box">
    <h3 class="contact-title"><strong>Contact</strong> Us</h3>
    <p class="contact-address">Bright Sprouts Accelerated<br>Learning Centre<br>Dubai, UAE</p>
    <p class="contact-phone"><span>Tel :</span> +971 500 123 456</p>
  </aside>

  <section class="talents">
    <div class="talent" style="left:18px">
      <div class="talent-label">Artist Ability</div>
      <svg class="talent-arrow" width="10" height="22" viewBox="0 0 10 22"><path d="M5 0v4M5 7v4M5 14v6M1 15l4 6 4-6" stroke="#3db8e3" stroke-width="2" fill="none"/></svg>
      <div class="talent-figure" role="img" aria-label="Illustration of a girl holding a paint palette and brush" style="background:linear-gradient(#c0643a,#f4e06a)"></div>
      <svg class="talent-stand" width="86" height="42" viewBox="0 0 86 42"><path d="M12 2h62l10 18H2z" fill="#5fcbef"/><rect x="0" y="20" width="86" height="20" rx="3" fill="var(--sky-blue)"/></svg>
    </div>
    <div class="talent" style="left:231px">
      <div class="talent-label">Sharp Imagination</div>
      <svg class="talent-arrow" width="10" height="22" viewBox="0 0 10 22"><path d="M5 0v4M5 7v4M5 14v6M1 15l4 6 4-6" stroke="#3db8e3" stroke-width="2" fill="none"/></svg>
      <div class="talent-figure" role="img" aria-label="Illustration of a boy crouching with a pinwheel" style="background:linear-gradient(#f2d04a,#3bb3a0)"></div>
      <svg class="talent-stand" width="86" height="42" viewBox="0 0 86 42"><path d="M12 2h62l10 18H2z" fill="#5fcbef"/><rect x="0" y="20" width="86" height="20" rx="3" fill="var(--sky-blue)"/></svg>
    </div>
    <div class="talent" style="left:424px">
      <div class="talent-label is-center">Your Kid</div>
      <svg class="talent-arrow" width="10" height="22" viewBox="0 0 10 22"><path d="M5 0v4M5 7v4M5 14v6M1 15l4 6 4-6" stroke="#3db8e3" stroke-width="2" fill="none"/></svg>
      <div class="talent-figure" role="img" aria-label="Blue silhouette of a child" style="background:#45b3cf"></div>
      <svg class="talent-stand" width="86" height="42" viewBox="0 0 86 42"><path d="M12 2h62l10 18H2z" fill="#5fcbef"/><rect x="0" y="20" width="86" height="20" rx="3" fill="var(--sky-blue)"/></svg>
    </div>
    <div class="talent" style="left:595px">
      <div class="talent-label">Dance Ability</div>
      <svg class="talent-arrow" width="10" height="22" viewBox="0 0 10 22"><path d="M5 0v4M5 7v4M5 14v6M1 15l4 6 4-6" stroke="#3db8e3" stroke-width="2" fill="none"/></svg>
      <div class="talent-figure" role="img" aria-label="Illustration of a dancing girl in a green dress" style="background:linear-gradient(#4a2a22,#b8d84a)"></div>
      <svg class="talent-stand" width="86" height="42" viewBox="0 0 86 42"><path d="M12 2h62l10 18H2z" fill="#5fcbef"/><rect x="0" y="20" width="86" height="20" rx="3" fill="var(--sky-blue)"/></svg>
    </div>
    <div class="talent" style="left:793px">
      <div class="talent-label">Sports Talent</div>
      <svg class="talent-arrow" width="10" height="22" viewBox="0 0 10 22"><path d="M5 0v4M5 7v4M5 14v6M1 15l4 6 4-6" stroke="#3db8e3" stroke-width="2" fill="none"/></svg>
      <div class="talent-figure" role="img" aria-label="Illustration of a boy playing with a football" style="background:linear-gradient(#a8552a,#e8d24a 55%,#3a7fc0)"></div>
      <svg class="talent-stand" width="86" height="42" viewBox="0 0 86 42"><path d="M12 2h62l10 18H2z" fill="#5fcbef"/><rect x="0" y="20" width="86" height="20" rx="3" fill="var(--sky-blue)"/></svg>
    </div>
  </section>

  <footer class="site-footer">
    <p class="copyright">Copyright © 2013 <strong>Bright Sprouts</strong>. All Right Reserved.</p>
    <div class="social-links">
      <div class="social-dot" role="img" aria-label="Social profile link" style="background:#3b5ea8"></div>
      <div class="social-dot" role="img" aria-label="Social profile link" style="background:#3fb6e6"></div>
      <svg class="social-dot" width="30" height="30" viewBox="0 0 30 30" role="img" aria-label="Email">
        <circle cx="15" cy="15" r="15" fill="#cfcfcf"/>
        <rect x="7" y="10" width="16" height="11" rx="1" fill="#ffffff" stroke="#666" stroke-width="1"/>
        <path d="M7.5 10.5 15 16.5l7.5-6" fill="none" stroke="#666" stroke-width="1"/>
      </svg>
    </div>
  </footer>
</body>
</html>
```